Agriculture Security Company needs a business card design

We need a business card design for a new company based in Seattle calls Corvantel Guard LLC. We provide high-end physical security solutions that is geared and focused towards to the marijuana grow operations, wholesalers and distributors. We DO NOT get involved in the retail operations (store fronts). We would like to see designs that incorporate professionalism, reliability, trustworthy and forward thinking as traits of our organization.

Industry/Entity Type

Security

```html
<!DOCTYPE html>
<html lang="en">
<head>
<meta charset="utf-8">
<title>Corvantel Guard LLC – Business Card</title>
<link href="https://fonts.googleapis.com/css2?family=Source+Sans+3:wght@400;600&display=swap" rel="stylesheet">
<style>
  :root {
    --backdrop: #e9e6e0;
    --card-white: #fbfbfa;
    --leaf-green: #6a9c3a;
    --deep-green: #2f7a3a;
    --rule-green: #3d7f2e;
    --text-white: #ffffff;
  }
  html, body {
    margin: 0;
    width: 1200px;
    height: 1023px;
    overflow: hidden;
    background: var(--backdrop);
    font-family: "Source Sans 3", Arial, sans-serif;
  }
  .canvas { position: relative; width: 1200px; height: 1023px; }
  .card {
    position: absolute;
    width: 640px;
    height: 366px;
    border-radius: 22px;
    overflow: hidden;
    box-shadow: 0 10px 28px rgba(0,0,0,0.18);
  }
  .card-front { left: 80px; top: 110px; background: var(--card-white); }
  .card-back { left: 480px; top: 545px; background: var(--leaf-green); }
  .front-shapes { position: absolute; inset: 0; }
  .brand {
    position: absolute;
    display: flex;
    align-items: center;
    gap: 12px;
    font-weight: 600;
    letter-spacing: 1px;
  }
  .brand-mark { border-radius: 50%; flex: none; }
  .card-front .brand { left: 44px; top: 118px; font-size: 34px; color: var(--deep-green); }
  .card-front .brand-mark { width: 26px; height: 26px; background: var(--deep-green); }
  .holder { position: absolute; right: 44px; top: 34px; text-align: right; }
  .holder-name { font-size: 24px; font-weight: 600; color: var(--deep-green); }
  .holder-title { font-size: 15px; color: var(--leaf-green); }
  .contact {
    position: absolute;
    color: var(--text-white);
    font-size: 14px;
    line-height: 1.35;
    text-align: center;
  }
  .contact strong { font-weight: 600; }
  .contact-email { left: 40px; top: 290px; width: 190px; }
  .contact-office { left: 230px; top: 256px; width: 210px; }
  .contact-web { left: 440px; top: 222px; width: 190px; }
  .card-back .brand {
    left: 0; right: 0; top: 140px;
    justify-content: center;
    font-size: 44px;
    color: var(--text-white);
  }
  .card-back .brand-mark { width: 32px; height: 32px; background: var(--text-white); }
  .back-web {
    position: absolute; left: 0; right: 0; bottom: 34px;
    text-align: center;
    color: var(--text-white);
    font-size: 15px;
    letter-spacing: 3px;
  }
</style>
</head>
<body>
<div class="canvas">

  <section class="card card-front" aria-label="Card front">
    <svg class="front-shapes" width="640" height="366" viewBox="0 0 640 366">
      <polygon points="0,250 640,150 640,366 0,366" fill="#6a9c3a"/>
      <line x1="0" y1="250" x2="640" y2="150" stroke="#3d7f2e" stroke-width="3"/>
      <g class="icon icon-email" transform="translate(130,230)">
        <circle r="19" fill="#6a9c3a" stroke="#fff" stroke-width="3"/>
        <rect x="-9" y="-6" width="18" height="12" fill="none" stroke="#fff" stroke-width="2"/>
        <polyline points="-9,-6 0,2 9,-6" fill="none" stroke="#fff" stroke-width="2"/>
      </g>
      <g class="icon icon-phone" transform="translate(330,198)">
        <circle r="19" fill="#6a9c3a" stroke="#fff" stroke-width="3"/>
        <path d="M-7,-8 q-3,10 6,16 l3,-3 -4,-4 -2,2 q-3,-3 -3,-7 l2,-1 -1,-5 z" fill="#fff"/>
      </g>
      <g class="icon icon-web" transform="translate(540,166)">
        <circle r="19" fill="#6a9c3a" stroke="#fff" stroke-width="3"/>
        <circle r="9" fill="none" stroke="#fff" stroke-width="2"/>
        <ellipse rx="4" ry="9" fill="none" stroke="#fff" stroke-width="1.5"/>
        <line x1="-9" y1="0" x2="9" y2="0" stroke="#fff" stroke-width="1.5"/>
      </g>
    </svg>

    <div class="brand"><span class="brand-mark"></span><span class="brand-name">Corvantel Guard</span></div>

    <div class="holder">
      <div class="holder-name">Dorian Welk</div>
      <div class="holder-title">President</div>
    </div>

    <div class="contact contact-email">info@corvantelguard.com</div>
    <div class="contact contact-office">555-014-2287<br><strong>Corvantel Guard LLC</strong><br>2180 Halvern Rd Tacoma Heights, WA 98402</div>
    <div class="contact contact-web">www.corvantelguard.com</div>
  </section>

  <section class="card card-back" aria-label="Card back">
    <div class="brand"><span class="brand-mark"></span><span class="brand-name">Corvantel Guard</span></div>
    <div class="back-web">www.corvantelguard.com</div>
  </section>

</div>
</body>
</html>
```